Need Business Card for our Indian Grocery Store

Industry/Entity Type

Grocery Store

Contact Information for Business Card

Manoj Baweja
Director

Store Locations:

Ashbury Vale
482 Elm Parade
P: 03 9172 5843

Kelvindale
613 Carlow Road
P: 03 9238 6014

email: kvtmarts@mailnest.example

Requirements
Must have
• Our logo Colours

```html
<!DOCTYPE html>
<html lang="en">
<head>
<meta charset="utf-8">
<title>KVT Marts – Business Card</title>
<link rel="stylesheet" href="https://fonts.googleapis.com/css2?family=Open+Sans:wght@400;600;700&display=swap">
<style>
  :root {
    --page-bg: #f5f5f5;
    --card-white: #ffffff;
    --pattern-light: #f7f7f7;
    --brand-red: #e31e24;
    --pattern-red: #e42a2f;
    --text-dark: #3f3f3f;
    --text-white: #ffffff;
  }
  * { box-sizing: border-box; margin: 0; padding: 0; }
  html, body {
    width: 1200px; height: 1000px; overflow: hidden;
    background: var(--page-bg);
    font-family: "Open Sans", Arial, sans-serif;
  }
  .canvas { position: relative; width: 1200px; height: 1000px; }

  .card {
    position: absolute; left: 257px; width: 688px; height: 392px;
    box-shadow: 2px 3px 5px rgba(0,0,0,0.28);
    overflow: hidden;
  }
  .card--front { top: 86px; background: var(--card-white); }
  .card--back { top: 520px; background: var(--brand-red); }

  .card__pattern { position: absolute; inset: 0; }
  .card--front .card__pattern { background: var(--pattern-light); }
  .card--back .card__pattern { background: var(--pattern-red); }

  .identity {
    position: absolute; left: 40px; width: 234px; top: 120px;
    text-align: center;
  }
  .brand-name {
    font-weight: 700; font-size: 34px; letter-spacing: 1px;
    color: var(--brand-red); line-height: 1.1;
  }
  .person-name {
    margin-top: 68px;
    font-weight: 600; font-size: 23px; letter-spacing: 0.8px;
    color: var(--brand-red); line-height: 1.1; text-transform: uppercase;
    white-space: nowrap;
  }
  .person-role {
    margin-top: 1px;
    font-size: 16px; letter-spacing: 1.6px;
    color: var(--text-dark); text-transform: uppercase;
  }

  .divider {
    position: absolute; left: 342px; top: 82px;
    width: 3px; height: 230px; background: var(--brand-red);
  }

  .locations { position: absolute; left: 473px; top: 103px; }
  .location { position: relative; margin-bottom: 33px; }
  .location__line {
    font-size: 18px; line-height: 24.5px; letter-spacing: 0.6px;
    color: var(--text-dark); white-space: nowrap;
  }
  .icon { position: absolute; left: -34px; fill: var(--brand-red); }
  .icon--pin { top: 5px; width: 16px; height: 24px; left: -32px; }
  .icon--phone { top: 53px; width: 20px; height: 16px; }

  .back-brand {
    position: absolute; left: 0; right: 0; top: 150px;
    text-align: center;
    font-weight: 700; font-size: 52px; letter-spacing: 2px;
    color: var(--text-white);
  }
  .back-email {
    position: absolute; left: 0; right: 0; top: 329px;
    text-align: center;
    font-size: 19px; letter-spacing: 0.4px;
    color: var(--text-white);
  }
</style>
</head>
<body>
<div class="canvas">

  <section class="card card--front">
    <div class="card__pattern" role="img" aria-label="Faint repeating pattern of small grocery shop-front icons"></div>

    <div class="identity">
      <div class="brand-name">KVT MARTS</div>
      <div class="person-name">Manoj Baweja</div>
      <div class="person-role">Director</div>
    </div>

    <div class="divider"></div>

    <div class="locations">
      <div class="location">
        <svg class="icon icon--pin" viewBox="0 0 16 24" aria-hidden="true">
          <path d="M8 0C3.6 0 0 3.5 0 7.9 0 13.5 8 24 8 24s8-10.5 8-16.1C16 3.5 12.4 0 8 0zm0 11a3.2 3.2 0 1 1 0-6.4A3.2 3.2 0 0 1 8 11z"/>
        </svg>
        <svg class="icon icon--phone" viewBox="0 0 20 16" aria-hidden="true">
          <path d="M2 5C2 2 6 1 10 1s8 1 8 4v1.5h-4V4.5H6V6.5H2z"/>
          <path d="M4 7h12l2 8H2z"/>
          <rect x="8" y="9" width="4" height="3" fill="#fff"/>
        </svg>
        <div class="location__line">Kelvindale</div>
        <div class="location__line">613 Carlow Road</div>
        <div class="location__line">03 9238 6014</div>
      </div>
      <div class="location">
        <svg class="icon icon--pin" viewBox="0 0 16 24" aria-hidden="true">
          <path d="M8 0C3.6 0 0 3.5 0 7.9 0 13.5 8 24 8 24s8-10.5 8-16.1C16 3.5 12.4 0 8 0zm0 11a3.2 3.2 0 1 1 0-6.4A3.2 3.2 0 0 1 8 11z"/>
        </svg>
        <svg class="icon icon--phone" viewBox="0 0 20 16" aria-hidden="true">
          <path d="M2 5C2 2 6 1 10 1s8 1 8 4v1.5h-4V4.5H6V6.5H2z"/>
          <path d="M4 7h12l2 8H2z"/>
          <rect x="8" y="9" width="4" height="3" fill="#fff"/>
        </svg>
        <div class="location__line">Ashbury Vale</div>
        <div class="location__line">482 Elm Parade</div>
        <div class="location__line">03 9172 5843</div>
      </div>
    </div>
  </section>

  <section class="card card--back">
    <div class="card__pattern" role="img" aria-label="Repeating pattern of grocery shop-front icons in lighter red"></div>
    <div class="back-brand">KVT MARTS</div>
    <div class="back-email">kvtmarts@mailnest.example</div>
  </section>

</div>
</body>
</html>
```